Business card for Northland's Blue Wagon.

Good day i am looking for a business card design for my business.
The name of the business is Northland's Blue Wagon. It is a van rental business that provides a driver and helper to the customer. Customer have use to van for small moves, studio or 1 bedroom, Moving furniture like couch or kitchen cabinets.
We are available evenings, weekends and holidays.
the means to contact us is by phone at 628-947-2071; By emails at Oakridge@northlandsbluewagon.net; or by social media, Circlenet and Photolane.
You can see attached pictures of the van and or logo.

```html
<!DOCTYPE html>
<html lang="en">
<head>
<meta charset="utf-8">
<title>Northland's Blue Wagon — Business Card</title>
<link rel="stylesheet" href="https://fonts.googleapis.com/css2?family=Open+Sans:wght@400;600&display=swap">
<style>
  :root {
    --page-bg: #ecebe8;
    --card-bg: #ffffff;
    --ink: #2a2a2a;
    --accent-red: #d3202b;
    --card-shadow: rgba(0, 0, 0, 0.16);
  }
  * { box-sizing: border-box; margin: 0; padding: 0; }
  html, body {
    width: 1200px;
    height: 780px;
    overflow: hidden;
    background: var(--page-bg);
    font-family: "Open Sans", Arial, sans-serif;
    color: var(--ink);
  }
  .card-sheet {
    width: 1200px;
    height: 780px;
    display: flex;
    align-items: center;
    justify-content: center;
    gap: 60px;
  }
  .business-card {
    position: relative;
    width: 525px;
    height: 300px;
    background: var(--card-bg);
    border-radius: 22px;
    box-shadow: 0 10px 26px var(--card-shadow);
  }
  .brand-mark {
    position: absolute;
    left: 50%;
    top: 50%;
    transform: translate(-50%, -50%);
    display: flex;
    align-items: center;
    gap: 18px;
  }
  .brand-mark__disc {
    width: 140px;
    height: 140px;
    border-radius: 50%;
    background: var(--accent-red);
    flex: none;
  }
  .brand-mark__name {
    font-weight: 600;
    font-size: 30px;
    line-height: 1.15;
    color: var(--accent-red);
    letter-spacing: 0.01em;
    white-space: nowrap;
  }
  .contact-card .brand-mark { top: 55%; }
  .contact-list {
    position: absolute;
    left: 24px;
    top: 18px;
    display: flex;
    gap: 24px;
    list-style: none;
    font-size: 15px;
  }
  .contact-list__item {
    display: flex;
    align-items: center;
    gap: 7px;
    white-space: nowrap;
  }
  .contact-list__icon {
    width: 13px;
    height: 13px;
    flex: none;
  }
  .social-list {
    position: absolute;
    right: 24px;
    bottom: 20px;
    display: flex;
    gap: 14px;
    list-style: none;
    font-size: 12px;
    font-weight: 600;
    color: var(--accent-red);
  }
  .social-list__item {
    display: flex;
    align-items: center;
    gap: 5px;
  }
  .social-list__dot {
    width: 14px;
    height: 14px;
    border-radius: 50%;
    background: var(--accent-red);
  }
</style>
</head>
<body>
<main class="card-sheet">
  <section class="business-card contact-card" aria-label="Card back with contact details">
    <ul class="contact-list">
      <li class="contact-list__item">
        <svg class="contact-list__icon" viewBox="0 0 24 24" aria-hidden="true">
          <path fill="var(--accent-red)" d="M6.6 10.8a15.1 15.1 0 0 0 6.6 6.6l2.2-2.2a1 1 0 0 1 1-.25 11.4 11.4 0 0 0 3.6.57 1 1 0 0 1 1 1V20a1 1 0 0 1-1 1A17 17 0 0 1 3 4a1 1 0 0 1 1-1h3.5a1 1 0 0 1 1 1c0 1.25.2 2.45.57 3.57a1 1 0 0 1-.25 1z"/>
        </svg>
        <span>628-947-2071</span>
      </li>
      <li class="contact-list__item">
        <svg class="contact-list__icon" viewBox="0 0 24 24" aria-hidden="true">
          <rect x="2" y="5" width="20" height="14" rx="2" fill="var(--accent-red)"/>
          <path d="M3 6l9 7 9-7" fill="none" stroke="#fff" stroke-width="2"/>
        </svg>
        <span>Oakridge@northlandsbluewagon.net</span>
      </li>
    </ul>
    <div class="brand-mark">
      <span class="brand-mark__disc"></span>
      <span class="brand-mark__name">Northland's<br>Blue Wagon</span>
    </div>
    <ul class="social-list">
      <li class="social-list__item"><span class="social-list__dot"></span>Circlenet</li>
      <li class="social-list__item"><span class="social-list__dot"></span>Photolane</li>
    </ul>
  </section>

  <section class="business-card logo-card" aria-label="Card front with brand name">
    <div class="brand-mark">
      <span class="brand-mark__disc"></span>
      <span class="brand-mark__name">Northland's<br>Blue Wagon</span>
    </div>
  </section>
</main>
</body>
</html>
```